Meadowlark Lane Yoga Facebook Design

"Practice Radiant Movement"

Foundational and sustainable yoga practice to cultivate growth through a variety of anatomy- informed movement patterns. Develop an informative and inspirational connection with the mind, body and spirit, through smart and integrated movement.

-I need a design that is happy and cheerful and attracts children and adults alike. I teach vinyassa based yoga that is sustainable and smart, kid yoga, and chair yoga.

-A movement practic rooted in foundation, core, and expression

- Accessible yoga for a sustained practice. A guided movement practice where one gains information and knowledge of oneself through a mind/body connection. For one feel good physically with a new awareness of their internal radiance that exists in all beings. Physical rejuvenation egnites a light and increases energy to flow through the physical body, which ultimately tranlates into works of kindness for others and out in the world.

Nora Whitfield
Yoga Instructor
MD, Pediatrician
RYT-200
RCYT
Certified yoga teacher for adults and children

Full description:
What is the positioning or mission statement of your company? to guide individuals in a yoga-based safe and sustainable movement practice applicable to all ages and body types. Currently my focus is working with children in daycare and school settings, but my goal is to expand into private yoga practice for adults, and potentially as part of rented space in studios. I hope to find a way to work with children AND adults (so would love for logo to be appealing to both), but current focus is with children based on need and demand in the community. yoga for children also compliments my backround as a pediatrician/neonatologist, and I greatly miss interacting with children. I also want to emphasize a yoga/movement practice that is focused more on what one feels internally through movement. NOT what one looks like asthetically. I believe in removing all mirrors from yoga/movement practice. It should be an experience of movement/poses/yoga through appropriate cueing and education. It is not about the details of how far the knee should bend, or how high the leg should be. Focusing on foudation first, core, then core engagement and ultimately expression of poses/movements. A focus on strength, stability and mobility, not just flexibility, which is the common perception/association with yoga. I also want individuals to learn to be an advocate of their own health. Through guidance, I hope for individuals to connect with their body so they know themselves so well to be able to advocate for themselves in the modern healthcare world. This internal experience and connection is so essential in a world where modern medicine has become a business and it is all about making a dollar. the connection with patients is lost, and individuals need to learn to empower themselves and through their new found voice to be able to articulate what is wrong.
Does your company have a tagline or slogan that should be included with the logo? "Practice Radiant Movement"
What do you hope your company can be known for? Accessible yoga for a sustained practice. A guided movement practice where one gains information and knowledge of oneself through a mind/body connection. For one feel good physically with a new awareness of their internal radiance that exists in all beings. Physical rejuvenation egnites a light and increases energy to flow through the physical body, which ultimately tranlates into works of kindness for others and out in the world.
What color palettes might you prefer? why? love the colors currently chosen
Where will the logo be primarily used? initially business cards, but hopefully future websites, t-shirts, and potentially local magazine adds. Also starting with a small couple of banners for community events in the area. I currently practice as a nomad out of my car :)
Are there any elements you would prefer to see in the logo? Movement. A modern depiction of a human body/figure practicing movement. Hoping to avoid a stereotypical yoga pose per say, just because I want to people to think of it more of a movement practice with yoga roots. Modern yoga. There are elements of breathing and connecting with oneself through the flow of breath and movement, but I do not focus on the meditative/cerebral aspect of the yoga practice. What I teach is almost reaching a meditative state through movement. I personally don't practice, nor resonate with just seated meditation. just not my thing :)
In your opinion, what defines a well-designed logo? curiosity. enough info for individuals to think they know what it means, but want to know more. invokes curiosity, but not too abstract. Reproducible. not too complicated. I want also to invoke a community feel, so a design that appeals to all people within a community.
What is your preference in reference to icons, typography, spokespeople (characters), etc.? modern design. I love the idea of a logo for my purposes, to invoke a sense of movement from within. So not too static.
What words or icons must be included in the logo? movement with yoga roots.
What logos do you like and why? A representation, but not exact. I think some ambiguity is intriguing for others, and also memorable. I want it to be an artistic representation of movement/yoga
What logos do you dislike and why? too busy, too loud.
In your opinion, what is the primary purpose for a logo? association
Who is the primary target audience? (who is most likely to use your services/product?) Children and their parents, but ultimately to expand into teaching adults. I even have aspirations of prenatal and post-natal yoga. Potentially incorporating infants.
Who currently uses your product the most? n/a (working in schools/daycare currently. It is currently all volunteer)
Are you pleased with the range of people your company serves? n/a
Are you looking to expand, modify, or completely change your target audience? or will it remain the same? yes! expand into an adult audience.
How do you plan to focus on your target audience? currently by working through schools and daycares. hopefully ultimately through after school care programs and then offering kid yoga in an existing yoga studio (working on this with Q studio in Ridgeland, currently)
What are your main forms of advertising? word of mouth, schools, daycares. Happy kids talking to their parents about the yoga class they took and happy teachers :)
How do most customers find out about your company?
Which gender are you targeting? All genders! However, with kid yoga, often the maternal individual in the child's life is more involved with decision making as far as extracurricular activities

Target Market(s)

Adults, children and families interested in movement, wellness and fun

Font styles to use
Sans Serif

Requirements
Must have
• ***I meant to emphasize the that "S" figure in my logo is SOOO iimportant to me. My daughter designed it. please highlight the "S" figure if possible******
My logo and the phrase "practice radiant movement"
Same colors as my logo
Feel like movement and fun.
Attracts children and families
Incorporate pieces of my description somehow
Nice to have
• different yoga poses or figures in movement
abstract design
attacts all body types and genders
inclusive

Industry is yoga, movement, wellness
Should not have
• no darkness
want happy and vibrant, inviting

```html
<!DOCTYPE html>
<html lang="en">
<head>
<meta charset="utf-8">
<title>Meadowlark Lane Yoga – Practice Radiant Movement</title>
<link href="https://fonts.googleapis.com/css2?family=Catamaran:wght@500;600;700;800&display=swap" rel="stylesheet">
<style>
  :root {
    --purple: #7a16b8;
    --purple-deep: #5d0d98;
    --purple-soft: #9a2fd0;
    --yellow: #f0c531;
    --yellow-deep: #e2b422;
    --white: #ffffff;
    --stage: #f4f1f6;
    --font: "Catamaran", sans-serif;
  }
  * { margin: 0; padding: 0; box-sizing: border-box; }
  html, body {
    width: 1200px; height: 800px; overflow: hidden;
    background: var(--stage);
    font-family: var(--font);
  }
  .stage {
    width: 1200px; height: 800px;
    display: flex; align-items: center; justify-content: center;
  }
  .post {
    position: relative;
    width: 668px; height: 760px;
    background: var(--purple);
    overflow: hidden;
  }
  .post__waves { position: absolute; inset: 0; width: 100%; height: 100%; }
  .post__email {
    position: absolute; top: 18px; right: 22px;
    font-size: 11px; font-weight: 600; color: var(--purple-deep);
  }
  .brand {
    position: absolute; top: 70px; left: 30px;
    display: flex; align-items: center; gap: 12px;
  }
  .brand__dot {
    width: 56px; height: 56px; border-radius: 50%;
    background: var(--yellow);
    flex-shrink: 0;
  }
  .brand__name {
    font-size: 26px; font-weight: 700; line-height: 1.05;
    color: var(--yellow);
    width: 170px;
  }
  .headline {
    position: absolute; left: 360px; top: 160px;
    font-weight: 700; line-height: 1.6;
  }
  .headline__lead { font-size: 31px; color: var(--white); display: block; }
  .headline__tag { font-size: 31px; color: var(--yellow); display: block; }
  .credential {
    position: absolute; left: 366px; top: 338px;
    font-size: 20px; font-weight: 700; line-height: 1.2;
    color: var(--white);
    padding-bottom: 8px;
    border-bottom: 4px solid var(--yellow);
    width: 214px;
  }
  .summary {
    position: absolute; left: 366px; top: 414px;
    width: 212px;
    font-size: 11px; font-weight: 500; line-height: 1.3;
    color: var(--white);
  }
  .cta {
    position: absolute; left: 376px; top: 536px;
    width: 240px; height: 48px; border-radius: 24px;
    background: var(--white);
    color: var(--purple);
    font-size: 15px; font-weight: 800; letter-spacing: 0.04em;
    display: flex; align-items: center; justify-content: center;
  }
  .illustration {
    position: absolute; left: 38px; top: 390px;
    width: 292px; height: 335px;
    border-radius: 24px;
    background: radial-gradient(ellipse at 50% 55%, #f7d866 0%, var(--yellow-deep) 70%, rgba(226,180,34,0) 100%);
  }
</style>
</head>
<body>
<main class="stage">
  <article class="post">
    <svg class="post__waves" viewBox="0 0 668 760" preserveAspectRatio="none" aria-hidden="true">
      <path d="M0 0 H668 V760 H0 Z" fill="var(--purple)"/>
      <path d="M120 0 C260 120 420 60 480 170 C540 280 600 300 668 300 V0 Z" fill="var(--purple-soft)" opacity="0.45"/>
      <path d="M350 0 C390 50 460 80 520 110 C590 145 630 190 668 225 V0 Z" fill="var(--yellow)"/>
      <path d="M0 330 C120 300 230 260 330 300 C450 350 540 420 668 400 V760 H0 Z" fill="var(--purple-deep)" opacity="0.35"/>
      <path d="M0 370 C90 350 200 380 270 450 C330 510 300 600 360 660 C390 700 410 730 420 760 H0 Z" fill="var(--yellow)"/>
    </svg>

    <p class="post__email">nora.whitfield@meadowlarkyoga.com</p>

    <div class="brand">
      <span class="brand__dot"></span>
      <span class="brand__name">Meadowlark Lane Yoga</span>
    </div>

    <h1 class="headline">
      <span class="headline__lead">Stay healthy</span>
      <span class="headline__tag">Practice</span>
      <span class="headline__tag">Radiant Movement</span>
    </h1>

    <p class="credential">Certified Yoga Teacher for Adults and Children</p>

    <p class="summary">Foundational and sustainable yoga practice to cultivate growth through a variety of anatomy- informed movement patterns.</p>

    <div class="cta">JOIN US NOW</div>

    <div class="illustration" role="img" aria-label="Illustration of an adult and children practising yoga poses together"></div>
  </article>
</main>
</body>
</html>
```